Word template Letterhead for Australian Law Firm

We are a small law firm based in Manly, NSW, Australia. We have had a new logo designed for us and wish to freshen up the appearance of our letterhead. We require the letterhead to be in a word document that we can type over. This will not be a ‘printed’ letterhead because we send the majority of our correspondence via email. We would like to see a few options. We have attached our previous letterhead as well as the artwork for our new logo. We like the idea of a watermark across the bottom of the letter but the watermark must stay in place and we must be able to type over it. We are open to some colour throughout the letterhead because the majority of our correspondence is sent electronically. We also use electronic signatures. I have uploaded an example of this.The letterhead must include:-1. Our address details – including our phone number, physical address, website address etc. These details can be found on the copy of our previous letterhead;2. ABN Number;3. The words ‘Corvenda (NSW) Pty Ltd ACN 742 185 903 trading as Shipton & AssociatesLiability limited by a scheme approved under Professional Standards Legislation. The letterhead does not need to include the names and qualifications of the people working at the firm. Thank you.

Target Market(s)

Clients and other parties

Industry/Entity Type

Law Firm

Font styles to use
Other font styles liked:
• raleway, montserrat

Colors

Designer to choose colors to be used in the design.

Requirements
Must have
• Certain wording - please see project description.
• Must be a word document and must be able to type over the watermark etc.
Nice to have
• Watermark at the bottom of the letter.

```html
<!DOCTYPE html>
<html lang="en">
<head>
<meta charset="utf-8">
<title>Ferrow &amp; Associates Letterhead</title>
<link rel="stylesheet" href="https://fonts.googleapis.com/css2?family=Montserrat:ital,wght@0,400;0,500;1,400&family=Raleway:wght@700&display=swap">
<style>
  :root {
    --backdrop: #f8f8f8;
    --paper: #ffffff;
    --paper-edge: #e2e2e6;
    --navy: #3c4590;
    --blue: #5a67b0;
    --gold: #c2a86e;
    --ink: #2b2b2b;
    --wash-blue: rgba(214, 219, 240, 0.75);
    --wash-blue-soft: rgba(225, 229, 244, 0.6);
    --wash-gold: rgba(240, 232, 212, 0.6);
    --clear: rgba(255, 255, 255, 0);
  }
  * { margin: 0; padding: 0; box-sizing: border-box; }
  html, body {
    width: 1200px; height: 912px; overflow: hidden;
    background: var(--backdrop);
  }
  .letterhead {
    position: absolute; left: 316px; top: 63px;
    width: 550px; height: 777px;
    background: var(--paper);
    border: 1px solid var(--paper-edge);
    overflow: hidden;
    font-family: "Montserrat", sans-serif;
  }
  .brand {
    position: absolute; left: 28px; top: 88px;
    width: 128px;
    display: flex; align-items: center; justify-content: center; gap: 5px;
  }
  .brand-dot {
    width: 6px; height: 6px; border-radius: 50%;
    background: var(--navy); flex: none;
  }
  .brand-name {
    font-family: "Raleway", sans-serif; font-weight: 700;
    font-size: 9.8px; letter-spacing: 1px; color: var(--ink);
    white-space: nowrap;
  }
  .rule { position: absolute; top: 0; width: 2px; }
  .rule-gold { left: 174px; height: 119px; background: var(--gold); }
  .rule-blue { left: 180px; height: 146px; background: var(--blue); }
  .contact {
    position: absolute; left: 206px; top: 38px;
    font-style: normal;
    font-size: 6.5px; letter-spacing: 0.5px; color: var(--navy);
    line-height: 9.8px;
  }
  .contact p { white-space: nowrap; }
  .contact .gap { margin-top: 3px; }
  .contact .label { color: var(--gold); }
  .watermark {
    position: absolute; left: 210px; top: 575px;
    width: 345px; height: 200px;
    background:
      radial-gradient(closest-side ellipse at 38% 48%, var(--wash-blue) 0%, var(--wash-blue-soft) 40%, var(--clear) 100%),
      radial-gradient(closest-side ellipse at 78% 40%, var(--wash-blue-soft) 0%, var(--clear) 100%),
      radial-gradient(closest-side ellipse at 80% 78%, var(--wash-gold) 0%, var(--clear) 100%);
    -webkit-mask-image: radial-gradient(closest-side ellipse at 55% 55%, #000 55%, transparent 100%);
            mask-image: radial-gradient(closest-side ellipse at 55% 55%, #000 55%, transparent 100%);
  }
  .footer-legal {
    position: absolute; right: 107px; top: 728px;
    text-align: right; font-size: 7.7px; letter-spacing: 0.2px;
    color: var(--navy); line-height: 10.6px;
  }
  .footer-legal .liability { font-style: italic; }
  .accreditation-badge {
    position: absolute; left: 458px; top: 723px;
    width: 36px; height: 36px; border-radius: 50%;
    background: var(--ink);
  }
</style>
</head>
<body>
  <main class="letterhead">
    <div class="brand">
      <span class="brand-dot"></span>
      <span class="brand-name">Ferrow &amp; Associates</span>
    </div>

    <div class="rule rule-gold"></div>
    <div class="rule rule-blue"></div>

    <address class="contact">
      <p>SUITE 4, 18 CORELLA STREET</p>
      <p>SEACLIFF, NSW 2097</p>
      <p class="gap"><span class="label">TELEPHONE:</span> (02) 9000 4118</p>
      <p><span class="label">FACSIMILE:</span> (02) 9000 4119</p>
      <p><span class="label">EMAIL:</span> reception@ferrowlaw.com.au</p>
      <p>ABN: 74 218 590 312</p>
      <p class="gap">www.ferrowandassociates.com.au</p>
    </address>

    <div class="watermark" role="img" aria-label="Faint brand watermark across the lower right of the page"></div>

    <footer class="footer-legal">
      <p>Corvenda (NSW) Pty Ltd ACN 742 185 903 trading as Ferrow &amp; Associates</p>
      <p class="liability">Liability limited by a scheme approved under Professional Standards Legislation</p>
    </footer>
    <div class="accreditation-badge" role="img" aria-label="Accreditation badge"></div>
  </main>
</body>
</html>
```